website design for small business consultancy - strategic research and writing

About the business
I am starting a new consultancy business called "Quill Harbor Consulting". I have asked for logo designs through Pixel Forum and am in the process of finalising these. I have a professional background and am an excellent and passionate writer and I want this professionalism conveyed through a modern, strong (confident) but simple, professional and elegant website. For SEO purposes, the services I will offer will include, but not be limited to, grants, submissions, proposals, strategic documents, complex correspondence, curriculum vitae and resumes, business cases, reports, training (grants and report writing). I will be based in Perth, Western Australia.

I would prefer the website be presented in black and white but I am not averse to colour, provided it's not gaudy. I want a header band across the top with the capacity to insert my logo (which I will send to the successful web builder) and the nature of the services "Strategic Research and Writing Services". I also want a net folio icon and a contact us button to the right (in the header).

I want a level one menu item underneath the header with the following menus - About (homepage), Services, Testimonials, and Contact (page to include a contact form).

I would like the following text to appear on the homepage as a highlight - like a drawcard for visitors to the site about my passion for what I do - "Lifting every idea into clear prose".

I want the capacity for a photo of me to be inserted on the About page.

I would like testimonials to feature distinctly, possibly in a box type format, either horizontally across the page or a couple or few in a row. There needs to be clear delineation of the person providing the testimonial and the testimonial itself.

Generally though I want a one column website that is accessible to those with disabilities. This is important to me as I believe all people should have access to website data.

I want the website to be responsive to tablets and mobile devices with high level SEO. One that is easy to add page headings to, and easy to amend and add plug ins. Maybe a wordpress site? The website must be compatible with Nimbo Webbing as I have paid for that.

Use of imagery is fine provided it is open source and relevant to the focus of the business.

Happy to send through further detail if required.

Thank you in anticipation. I have appreciated the work submitted to date.

I will insert the content (yet to be drafted)

Target Market(s)

Local government, private business, government

Contact Information for Business Card

Business card - I would like the logo on the front along with Strategic Research and Writing Services. I want the contact details on the back including: my name, role, email, mobile, web address, address.

I wouldn't mind a side panel on the rear in the colour of the business card with "Lifting every idea into clear prose" on it. Maybe with the text going up vertically. I can get the logo in black and white. I will upload the logo asap.

Coding

Number of Pages Required

Font styles to use
Serif
Sans Serif
Script

Requirements
Must have
• I want an elegant business card, professional but modern, that accords in branding to the website.
Should not have
• I do not want to use the red and black logo thanks. Either of the others is fine.

```html
<!DOCTYPE html>
<html lang="en">
<head>
<meta charset="utf-8">
<title>Quill Harbor Consulting — Strategic Research and Writing Services</title>
<link rel="stylesheet" href="https://fonts.googleapis.com/css2?family=Montserrat:wght@400;600;700&family=Open+Sans:wght@400;600;700&display=swap">
<style>
:root{
  --brand:#1d6394;
  --brand-dark:#154c73;
  --ink:#222;
  --text:#666;
  --muted:#999;
  --light:#f3f3f3;
  --line:#e4e4e4;
  --footer:#2d2d2d;
  --footer-bar:#232323;
  --white:#fff;
}
*{margin:0;padding:0;box-sizing:border-box}
html,body{width:1200px;height:3652px;overflow:hidden}
body{font-family:"Open Sans",Arial,sans-serif;color:var(--text);background:var(--white);position:relative}
h1,h2,h3,h4,.btn,.nav a{font-family:"Montserrat",Arial,sans-serif}
.btn{display:inline-block;background:var(--brand);color:var(--white);font-size:12px;font-weight:700;letter-spacing:.5px;text-transform:uppercase;padding:12px 26px;border-radius:22px;text-decoration:none}
.btn-outline{background:transparent;border:2px solid var(--white)}
.eyebrow{font-size:10px;font-weight:700;color:var(--brand);text-transform:uppercase;letter-spacing:1px;display:flex;align-items:center;gap:8px}
.eyebrow::before{content:"";width:60px;height:1px;background:var(--brand)}
.centered .eyebrow{justify-content:center}

/* header */
.site-header{position:absolute;top:0;left:0;width:1200px;height:110px;display:flex;align-items:center;justify-content:space-between;padding:0 80px 0 100px}
.brand{display:flex;align-items:center;gap:10px}
.brand-dot{width:34px;height:34px;border-radius:50%;background:var(--brand)}
.brand-name{font-family:"Montserrat",sans-serif;font-weight:700;font-size:19px;color:var(--brand);line-height:1.1}
.brand-tag{font-size:10px;color:var(--muted);letter-spacing:1px;text-transform:uppercase}
.nav{display:flex;align-items:center;gap:34px}
.nav a{font-size:12px;font-weight:600;color:var(--ink);text-decoration:none;text-transform:uppercase}
.nav a.active{color:var(--brand);border-bottom:2px solid var(--brand);padding-bottom:6px}
.social{display:flex;align-items:center;gap:6px;font-size:11px;color:var(--ink)}
.social span.dot{width:20px;height:20px;border-radius:50%;background:var(--ink)}
.nav .btn{color:var(--white);padding:10px 20px;font-size:11px}

/* hero */
.hero{position:absolute;top:110px;left:0;width:1200px;height:640px;background:linear-gradient(135deg,#d8d8d8 0%,#8e8e8e 45%,#4a4a4a 100%);text-align:center;color:var(--white)}
.hero-photo{position:absolute;inset:0}
.hero-content{position:relative;padding-top:240px}
.hero h1{font-size:42px;font-weight:700;text-transform:uppercase;letter-spacing:.5px}
.hero p{font-size:15px;margin:10px auto 36px;width:820px}
.hero .dots{position:absolute;left:0;right:0;top:548px;display:flex;justify-content:center;gap:10px}
.dots span{width:9px;height:9px;border-radius:50%;background:var(--white);opacity:.6}
.dots span.on{opacity:1}
.hero svg.wave{position:absolute;left:0;bottom:0}

/* partner strip */
.partners{position:absolute;top:750px;left:0;width:1200px;height:150px;display:flex;align-items:center;justify-content:center;gap:70px;border-bottom:1px solid var(--line)}
.partners .arrow{color:var(--muted);font-size:26px}
.partner-badge{width:100px;height:38px;background:#cfcfcf;border-radius:4px}

/* welcome */
.welcome{position:absolute;top:900px;left:0;width:1200px;height:550px}
.welcome-art{position:absolute;left:135px;top:110px;width:320px;height:320px;border-radius:50%;background:radial-gradient(circle,#3a82b6 0%,var(--brand) 55%,#dcdcdc 56%,#f0f0f0 100%)}
.welcome-copy{position:absolute;left:630px;top:135px;width:480px}
.welcome-copy h2{font-size:24px;color:var(--ink);margin:12px 0 14px;white-space:nowrap}
.welcome-copy p{font-size:13px;line-height:1.7;margin-bottom:26px;width:450px}

/* services */
.services{position:absolute;top:1450px;left:0;width:1200px;height:800px;background:var(--light);text-align:center}
.services .head{padding-top:90px}
.services h2{font-size:26px;color:var(--ink);margin:12px 0 10px}
.services .head p{font-size:13px;width:560px;margin:0 auto;line-height:1.6}
.service-card{position:absolute;top:250px;width:400px;height:480px;background:var(--white);box-shadow:0 2px 10px rgba(0,0,0,.08);padding:55px 50px 0}
.service-card.left{left:160px}
.service-card.right{left:640px}
.service-icon{width:130px;height:130px;border-radius:50%;border:6px solid #cfdde8;background:var(--brand);margin:0 auto 30px;display:flex;align-items:center;justify-content:center}
.service-card h3{font-size:16px;color:var(--ink);text-transform:uppercase;margin-bottom:14px}
.service-card p{font-size:13px;line-height:1.7;margin-bottom:26px}

/* about band */
.about-band{position:absolute;top:2250px;left:0;width:1200px;height:410px;background:linear-gradient(180deg,#5a5a5a,#3b3b3b);color:var(--white);text-align:center;padding-top:80px}
.about-photo{position:absolute;inset:0}
.about-inner{position:relative}
.about-band .eyebrow{color:var(--white)}
.about-band .eyebrow::before{background:var(--white)}
.about-band h2{font-size:28px;width:620px;margin:12px auto 16px;line-height:1.3}
.about-band p{font-size:13px;width:620px;margin:0 auto 28px;line-height:1.6;opacity:.85}

/* testimonials */
.testimonials{position:absolute;top:2660px;left:0;width:1200px;height:550px;text-align:center}
.testimonials .head{padding-top:95px}
.testimonials h2{font-size:28px;color:var(--ink);margin-top:8px}
.quote{position:absolute;top:190px;width:350px;text-align:center}
.quote .box{height:210px;background:var(--white);box-shadow:0 2px 12px rgba(0,0,0,.1);padding:50px 36px;font-size:12px;line-height:1.7}
.quote .who{display:flex;align-items:center;gap:14px;margin:20px 0 0 50px;text-align:left}
.avatar{width:48px;height:48px;border-radius:50%;background:#9a9a9a}
.who strong{display:block;font-family:"Montserrat",sans-serif;font-size:14px;color:var(--brand)}
.who span{font-size:11px;color:var(--muted)}
.testimonials .dots{position:absolute;top:515px;left:0;right:0;display:flex;justify-content:center;gap:8px}
.testimonials .dots span{background:#bbb;opacity:1;width:8px;height:8px}
.testimonials .dots span.on{background:var(--brand)}

/* footer */
.site-footer{position:absolute;top:3210px;left:0;width:1200px;height:442px;background:var(--footer);color:#bdbdbd}
.footer-cols{display:flex;padding:90px 0 0 110px}
.footer-col h4{font-size:20px;color:var(--white);font-weight:600;margin-bottom:20px}
.footer-col ul{list-style:none}
.footer-col li{font-size:12px;margin-bottom:9px;display:flex;align-items:center;gap:8px}
.footer-col li::before{content:"";flex:none;width:5px;height:5px;border-radius:50%;background:var(--brand)}
.footer-col.contact li::before{width:9px;height:9px}
.footer-col p{font-size:12px;margin-bottom:14px}
.signup{display:flex;width:250px}
.signup span{flex:1;background:var(--brand);color:var(--white);font-size:11px;padding:9px 12px}
.signup b{width:42px;background:var(--brand-dark)}
.footer-bar{position:absolute;bottom:0;left:0;width:1200px;height:56px;background:var(--footer-bar);display:flex;align-items:center;justify-content:space-between;padding:0 110px;font-size:11px}
.footer-bar nav{display:flex;gap:30px}
</style>
</head>
<body>

<header class="site-header">
  <div class="brand">
    <span class="brand-dot"></span>
    <div>
      <div class="brand-name">Quill Harbor Consulting</div>
      <div class="brand-tag">Strategic Research and Writing Services</div>
    </div>
  </div>
  <nav class="nav">
    <a href="#" class="active">Home</a>
    <a href="#">About Us</a>
    <a href="#">Services</a>
    <a href="#">Testimonials</a>
    <span class="social"><span class="dot"></span>net folio</span>
    <a href="#" class="btn">Contact Us</a>
  </nav>
</header>

<section class="hero">
  <div class="hero-photo" role="img" aria-label="Greyscale photo of hands typing on a laptop keyboard at a desk"></div>
  <div class="hero-content">
    <h1>Lifting every idea into clear prose</h1>
    <p>Clear documents shaped with care for councils, agencies and growing businesses across the state.</p>
    <a href="#" class="btn">Learn More</a>
  </div>
  <div class="dots"><span></span><span class="on"></span><span></span><span></span></div>
  <svg class="wave" width="1200" height="70" viewBox="0 0 1200 70" aria-hidden="true">
    <path d="M0 40 Q600 -10 1200 40 L1200 70 L0 70Z" fill="#fff"/>
    <path d="M0 40 Q600 -10 1200 40" fill="none" stroke="#1d6394" stroke-width="2"/>
  </svg>
</section>

<section class="partners" aria-label="Client badges">
  <span class="arrow">‹</span>
  <span class="partner-badge"></span><span class="partner-badge"></span><span class="partner-badge"></span>
  <span class="partner-badge"></span><span class="partner-badge"></span><span class="partner-badge"></span>
  <span class="arrow">›</span>
</section>

<section class="welcome">
  <div class="welcome-art" role="img" aria-label="Circular illustration of business and writing tools around a blue hub"></div>
  <div class="welcome-copy">
    <div class="eyebrow">Welcome To</div>
    <h2>What is Quill Harbor Consulting</h2>
    <p>Lorem ipsum dolor sit amet, consectetur adipiscing elit, sed do eiusmod tempor incididunt ut labore et dolore magna aliqua. Ut enim ad minim veniam, quis nostrud exercitation ullamco laboris nisi ut aliquip ex ea commodo consequat. Duis aute irure dolor in reprehenderit in voluptate velit esse cillum dolore eu fugiat nulla pariatur. Excepteur sint occaecat cupidatat non proident.</p>
    <a href="#" class="btn">Read More Information</a>
  </div>
</section>

<section class="services centered">
  <div class="head">
    <div class="eyebrow">Our Services</div>
    <h2>Magnam aliquam quaerat voluptatem</h2>
    <p>At vero eos et accusamus et iusto odio dignissimos ducimus qui blanditiis praesentium voluptatum deleniti atque corrupti quos dolores.</p>
  </div>
  <article class="service-card left">
    <div class="service-icon">
      <svg width="60" height="60" viewBox="0 0 60 60" aria-hidden="true"><circle cx="30" cy="30" r="24" fill="none" stroke="#fff" stroke-width="4"/><circle cx="30" cy="30" r="14" fill="none" stroke="#fff" stroke-width="4"/><circle cx="30" cy="30" r="4" fill="#fff"/><path d="M30 30 L52 8" stroke="#fff" stroke-width="3"/></svg>
    </div>
    <h3>Strategic Research</h3>
    <p>Lorem ipsum dolor sit amet, consectetur adipiscing elit, sed do eiusmod tempor incididunt ut labore et dolore magna aliqua enim ad minim veniam.</p>
    <a href="#" class="btn">Learn More</a>
  </article>
  <article class="service-card right">
    <div class="service-icon">
      <svg width="60" height="60" viewBox="0 0 60 60" aria-hidden="true"><rect x="12" y="8" width="30" height="42" rx="2" fill="none" stroke="#fff" stroke-width="4"/><path d="M18 20h18M18 28h18M18 36h10" stroke="#fff" stroke-width="3"/><path d="M38 46 L52 30" stroke="#fff" stroke-width="5"/></svg>
    </div>
    <h3>Writing Services</h3>
    <p>Lorem ipsum dolor sit amet, consectetur adipiscing elit, sed do eiusmod tempor incididunt ut labore et dolore magna aliqua enim ad minim veniam.</p>
    <a href="#" class="btn">Learn More</a>
  </article>
</section>

<section class="about-band centered">
  <div class="about-photo" role="img" aria-label="Darkened photo of a team working in an office"></div>
  <div class="about-inner">
    <div class="eyebrow">About Us</div>
    <h2>Temporibus autem quibusdam et aut officiis debitis aut rerum</h2>
    <p>At vero eos et accusamus et iusto odio dignissimos ducimus qui blanditiis praesentium voluptatum deleniti atque corrupti quos dolores et quas.</p>
    <a href="#" class="btn btn-outline">Read More Information</a>
  </div>
</section>

<section class="testimonials centered">
  <div class="head">
    <div class="eyebrow">Clients' Testimonials</div>
    <h2>Over the million people trust us</h2>
  </div>
  <figure class="quote" style="left:75px">
    <blockquote class="box">Ut ullamcorper nunc eget tempor cursus, neque elit consequat nisi, in ultricies massa est quis tortor. Donec sed tellus lorem, tempus eu feugiat aliquet nec.</blockquote>
    <figcaption class="who"><span class="avatar"></span><div><strong>By Author</strong><span>City, Location</span></div></figcaption>
  </figure>
  <figure class="quote" style="left:425px">
    <blockquote class="box">Ut ullamcorper nunc eget tempor cursus, neque elit consequat nisi, in ultricies massa est quis tortor. Donec sed tellus lorem, tempus eu feugiat aliquet nec.</blockquote>
    <figcaption class="who"><span class="avatar"></span><div><strong>By Author</strong><span>City, Location</span></div></figcaption>
  </figure>
  <figure class="quote" style="left:775px">
    <blockquote class="box">Ut ullamcorper nunc eget tempor cursus, neque elit consequat nisi, in ultricies massa est quis tortor. Donec sed tellus lorem, tempus eu feugiat aliquet nec.</blockquote>
    <figcaption class="who"><span class="avatar"></span><div><strong>By Author</strong><span>City, Location</span></div></figcaption>
  </figure>
  <div class="dots"><span class="on"></span><span></span><span></span></div>
</section>

<footer class="site-footer">
  <div class="footer-cols">
    <div class="footer-col" style="width:220px">
      <h4>Quick Link</h4>
      <ul><li>Home</li><li>About Us</li><li>Services</li><li>Testimonials</li><li>Blog</li><li>Contact</li></ul>
    </div>
    <div class="footer-col" style="width:230px">
      <h4>More Info</h4>
      <ul><li>Solutions</li><li>Our Map</li><li>News</li><li>Our Team</li><li>FAQ's</li><li>Business</li></ul>
    </div>
    <div class="footer-col contact" style="width:330px">
      <h4>Address</h4>
      <ul><li>Lorem ipsum dolor sit amet, consectetur adipiscing elit</li><li>+(61) 08 5550 1234</li><li>hello@quillharbor.example</li></ul>
    </div>
    <div class="footer-col">
      <h4>Join Our Mailing List</h4>
      <p>Subscribe to get latest updates</p>
      <div class="signup"><span>Enter email address</span><b></b></div>
    </div>
  </div>
  <div class="footer-bar">
    <span>Copyright © 2019 Quill Harbor Consulting. All Rights Reserved.</span>
    <nav><span>Terms of Use</span><span>Privacy Policy</span></nav>
  </div>
</footer>

</body>
</html>
```